Innovative Funky Australian Start Up - HR & Recruitment

We would like a brochure for our company "Crew Harbor". We provide affordable HR & Recruitment support for Small to Medium businesses.
We like a simple, fresh, crisp, clean look. Nothing overly complicated.
Target market is Small and medium businesses with 2-50 employees, this could be in IT, Accounting, Construction, Marketing or a Engineering, so really trying to appeal to all industries. We don’t want to come across as too high end corporate – more everyday professional. I’d say our target client is probably late 30’s to late 40’s owner or general manager
Our website is - www.crewharbor-example.com.au

Target Market(s)

Small and medium size business's.
Business owners.
Multiple industries

Industry/Entity Type

It Company

Font styles to use
Sans Serif

```html
<!DOCTYPE html>
<html lang="en">
<head>
<meta charset="utf-8">
<title>Crew Harbor – HR &amp; Recruitment Brochure Spread</title>
<link rel="stylesheet" href="https://fonts.googleapis.com/css2?family=Jost:wght@300;400;500&display=swap">
<style>
  :root {
    --backdrop: #2b2b2d;
    --paper: #f4f6f9;
    --navy: #2d5282;
    --navy-deep: #264a78;
    --sky: #4a90d9;
    --text-light: #ffffff;
    --text-soft: #dfe8f3;
    --bullet-red: #d9534f;
    --photo-office: #c9d4df;
    --photo-desk: #e4e7ec;
  }
  * { box-sizing: border-box; margin: 0; padding: 0; }
  html, body { width: 1200px; height: 789px; overflow: hidden; }
  body {
    background: var(--backdrop);
    font-family: "Jost", "Futura", sans-serif;
    font-weight: 300;
    color: var(--text-light);
    position: relative;
  }
  .spread {
    position: absolute;
    left: 60px; top: 34px;
    width: 1080px; height: 720px;
    display: flex;
    box-shadow: 0 18px 40px rgba(0,0,0,.5);
  }
  .page {
    position: relative;
    width: 540px; height: 720px;
    background: var(--paper);
    overflow: hidden;
  }
  .page--left::after {
    content: ""; position: absolute; right: 0; top: 0; bottom: 0; width: 30px;
    background: linear-gradient(to right, rgba(0,0,0,0), rgba(0,0,0,.18));
  }
  .page--right::before {
    content: ""; position: absolute; left: 0; top: 0; bottom: 0; width: 30px; z-index: 5;
    background: linear-gradient(to left, rgba(0,0,0,0), rgba(0,0,0,.15));
  }
  .shape { position: absolute; inset: 0; width: 100%; height: 100%; }

  /* Left page */
  .services { position: absolute; left: 44px; top: 40px; width: 460px; }
  .services__title { font-size: 17px; font-weight: 400; line-height: 1.2; }
  .services__sub { font-size: 9px; color: var(--text-soft); margin: 4px 0 10px; }
  .services__heading { font-size: 13px; font-weight: 400; margin-bottom: 4px; }
  .policy-list { list-style: none; font-size: 11px; line-height: 1.42; color: var(--text-soft); margin-bottom: 12px; }
  .policy-list li { position: relative; padding-left: 18px; }
  .policy-list li::before {
    content: ""; position: absolute; left: 2px; top: 4px; width: 8px; height: 8px;
    border-radius: 50%; background: #fff; border: 2px solid var(--bullet-red);
  }
  .services__para { font-size: 11.5px; line-height: 1.35; margin-bottom: 8px; max-width: 400px; }
  .photo { position: absolute; }
  .photo--team {
    left: 0; top: 470px; width: 540px; height: 250px;
    background: linear-gradient(120deg, #aebfd0 0%, var(--photo-office) 40%, #eef2f6 75%, #b8c6d4 100%);
  }
  .photo--desk {
    left: 0; top: 0; width: 540px; height: 300px;
    background: linear-gradient(160deg, #ffffff 0%, var(--photo-desk) 60%, #cfd6de 100%);
  }

  /* Right page */
  .about { position: absolute; left: 40px; top: 340px; width: 460px; }
  .about__title { font-size: 20px; font-weight: 400; margin-bottom: 12px; }
  .about__para { font-size: 9.5px; line-height: 1.42; color: var(--text-soft); margin-bottom: 8px; }
  .about__heading { font-size: 13px; font-weight: 400; margin: 10px 0 4px; }
  .about__heading strong { font-size: 17px; font-weight: 400; }
  .praise-list { list-style: none; font-size: 10.5px; line-height: 1.45; color: var(--text-soft); }
  .praise-list li { display: flex; align-items: center; gap: 6px; }
  .praise-list svg { width: 9px; height: 9px; flex: none; }
</style>
</head>
<body>
  <main class="spread">
    <section class="page page--left">
      <svg class="shape" viewBox="0 0 540 720" preserveAspectRatio="none" aria-hidden="true">
        <rect x="0" y="0" width="540" height="470" fill="var(--navy)"/>
        <polygon points="0,380 0,470 230,470" fill="var(--sky)"/>
      </svg>
      <div class="services">
        <h2 class="services__title">Crew Harbor Provide Comprehensive Templates &amp; Customised:</h2>
        <p class="services__sub">Contracts of Employment for Full time, Part time and &amp; Casual employees</p>
        <h3 class="services__heading">Essential Policies &amp; Procedures such as:</h3>
        <ul class="policy-list">
          <li>Use of IT, Internet, Email &amp; Social Media</li>
          <li>Code of Conduct</li>
          <li>Drug &amp; Alcohol</li>
          <li>Occupational Health &amp; Safety</li>
          <li>Bullying, Sexual Harassment</li>
          <li>Attendance &amp; Punctuality</li>
          <li>Leave</li>
          <li>Equal Opportunity of Employment, Diversity</li>
          <li>Corrective Action &amp; Discipline</li>
        </ul>
        <p class="services__para">Recruitment &amp; New Employee Documents such as interview guides, reference check forms and induction checklists.</p>
        <p class="services__para">Staff Management Documentations including probation, warning, termination &amp; redundancy letters.</p>
      </div>
      <div class="photo photo--team" role="img" aria-label="Photo of a smiling businessman holding his jacket over his shoulder with colleagues in an office behind him"></div>
    </section>

    <section class="page page--right">
      <div class="photo photo--desk" role="img" aria-label="Photo of a smiling businesswoman in a dark suit seated at a desk with a keyboard and monitor"></div>
      <svg class="shape" viewBox="0 0 540 720" preserveAspectRatio="none" aria-hidden="true">
        <polygon points="0,190 0,300 190,300" fill="var(--sky)"/>
        <rect x="0" y="300" width="540" height="420" fill="var(--navy)"/>
      </svg>
      <div class="about">
        <h2 class="about__title">Why We’re Different</h2>
        <p class="about__para">We’re just like you, and we want to see your business grow, develop and be successful. We want to really get to know you, your business and your staff, to assist in managing any issues that arise, and to help you develop engaged, productive teams.</p>
        <p class="about__para">Our team is made up of highly experienced, educated, capable and exceptionally dedicated people, predominately working Mum’s. Each member of our team has over 12 years’ experience within highly technical, demanding corporate careers.</p>
        <p class="about__para">You see, we believe in how capable and driven working parents are, and we’re tapping into that huge resource of experienced people who simply want the flexibility to work around the needs of their family.</p>
        <p class="about__para">We believe that through our hiring processes, and how we manage people – we can change the world. We promote our company values at every opportunity, because we know values and core beliefs are also what drive productivity and success in business as well.</p>
        <h3 class="about__heading">Our clients say <strong>We:</strong></h3>
        <ul class="praise-list">
          <li><svg viewBox="0 0 10 10"><path d="M1 5.5 L4 8.5 L9 1.5" fill="none" stroke="#fff" stroke-width="1.4"/></svg>Are Transparent, Ethical</li>
          <li><svg viewBox="0 0 10 10"><path d="M1 5.5 L4 8.5 L9 1.5" fill="none" stroke="#fff" stroke-width="1.4"/></svg>Knowledgeable, Down to Earth</li>
          <li><svg viewBox="0 0 10 10"><path d="M1 5.5 L4 8.5 L9 1.5" fill="none" stroke="#fff" stroke-width="1.4"/></svg>Committed, Personalised</li>
          <li><svg viewBox="0 0 10 10"><path d="M1 5.5 L4 8.5 L9 1.5" fill="none" stroke="#fff" stroke-width="1.4"/></svg>Fast, Flexible</li>
          <li><svg viewBox="0 0 10 10"><path d="M1 5.5 L4 8.5 L9 1.5" fill="none" stroke="#fff" stroke-width="1.4"/></svg>Have Exceptional Service &amp; Quality</li>
        </ul>
      </div>
    </section>
  </main>
</body>
</html>
```